Color palette UI design and CSS

I need a color palette design and the CSS implementation for the main UI components.
This is for a legal company and the concepts they want reflected are sophistication, elegance, minimalistic.
Attached is the company logo and an example of what you should deliver. In case of winning the contest you must implement the CSS.

```html
<!DOCTYPE html>
<html lang="en">
<head>
<meta charset="UTF-8">
<title>Color Palette</title>
<link rel="stylesheet" href="https://fonts.googleapis.com/css2?family=Source+Sans+3:wght@400&display=swap">
<style>
  :root {
    --canvas: #ffffff;
    --ink: #111111;
    --primary-blue: #25AAE2;
    --primary-white: #FAFFFF;
    --primary-charcoal: #333333;
    --secondary-green: #2CA988;
    --secondary-mint: #B1F3E2;
    --accent-violet: #5E2FBB;
    --accent-lavender: #9765FA;
    --dark-charcoal: #333333;
    --dark-navy: #092B39;
  }
  * { margin: 0; padding: 0; box-sizing: border-box; }
  html, body {
    width: 751px;
    height: 1200px;
    overflow: hidden;
    background: var(--canvas);
  }
  body {
    position: relative;
    font-family: "Source Sans 3", sans-serif;
    color: var(--ink);
  }
  .palette-title {
    position: absolute;
    top: 80px;
    left: 0;
    width: 100%;
    text-align: center;
    font-size: 29px;
    font-weight: 400;
    letter-spacing: 0.2px;
  }
  .brand-mark {
    position: absolute;
    top: 148px;
    left: 0;
    width: 100%;
    display: flex;
    justify-content: center;
    align-items: center;
    gap: 14px;
  }
  .brand-square {
    width: 58px;
    height: 58px;
    background: var(--primary-blue);
  }
  .brand-name {
    font-size: 56px;
    font-weight: 400;
    color: var(--primary-charcoal);
    line-height: 1;
    letter-spacing: 2px;
  }
  .swatch-group {
    position: absolute;
    left: 161px;
  }
  .group-label {
    font-size: 18px;
    font-weight: 400;
    line-height: 1;
    margin-bottom: 22px;
  }
  .swatch-row {
    display: flex;
    gap: 28px;
  }
  .swatch {
    width: 98px;
    display: flex;
    flex-direction: column;
    align-items: center;
  }
  .swatch-chip {
    width: 98px;
    height: 98px;
    border-radius: 50%;
  }
  .swatch-code {
    margin-top: 15px;
    font-size: 18px;
    line-height: 1;
    white-space: nowrap;
  }
  .swatch-code.is-low { margin-top: 28px; }
  .group-primary { top: 281px; }
  .group-secondary { top: 489px; }
  .group-accent { top: 696px; }
  .group-dark { top: 902px; }
</style>
</head>
<body>
  <h1 class="palette-title">COLOR PALETTE</h1>

  <div class="brand-mark">
    <span class="brand-square"></span>
    <span class="brand-name">RV&amp;ASOC</span>
  </div>

  <section class="swatch-group group-primary">
    <h2 class="group-label">Primary</h2>
    <div class="swatch-row">
      <div class="swatch"><span class="swatch-chip" style="background: var(--primary-blue)"></span><span class="swatch-code">#25AAE2</span></div>
      <div class="swatch"><span class="swatch-chip" style="background: var(--primary-white)"></span><span class="swatch-code">#FAFFFF</span></div>
      <div class="swatch"><span class="swatch-chip" style="background: var(--primary-charcoal)"></span><span class="swatch-code">#333333</span></div>
    </div>
  </section>

  <section class="swatch-group group-secondary">
    <h2 class="group-label">Secondary</h2>
    <div class="swatch-row">
      <div class="swatch"><span class="swatch-chip" style="background: var(--secondary-green)"></span><span class="swatch-code">#2CA988</span></div>
      <div class="swatch"><span class="swatch-chip" style="background: var(--secondary-mint)"></span><span class="swatch-code">#B1F3E2</span></div>
    </div>
  </section>

  <section class="swatch-group group-accent">
    <h2 class="group-label">Accent</h2>
    <div class="swatch-row">
      <div class="swatch"><span class="swatch-chip" style="background: var(--accent-violet)"></span><span class="swatch-code">#5E2FBB</span></div>
      <div class="swatch"><span class="swatch-chip" style="background: var(--accent-lavender)"></span><span class="swatch-code">#9765FA</span></div>
    </div>
  </section>

  <section class="swatch-group group-dark">
    <h2 class="group-label">Dark Tones</h2>
    <div class="swatch-row">
      <div class="swatch"><span class="swatch-chip" style="background: var(--dark-charcoal)"></span><span class="swatch-code is-low">#333333</span></div>
      <div class="swatch"><span class="swatch-chip" style="background: var(--dark-navy)"></span><span class="swatch-code is-low">#092B39</span></div>
    </div>
  </section>
</body>
</html>
```